New Equipment Rental Location Postcard *

We have a new equipment rental location that we opened and want to do a bulk mailing with a postcard to advertise. The post card has to be 6.5" x 9" and printed on both sides. The back side has to have the postage icons on them like in the example postcard I have uploaded. Also I have included our logo in the attachments. The attachement "capture' is just an example of how the back should look with the 2 postage icons. I have also uploaded those 2 graphics.

Rental

• I would like to convey "New Location". Also would like our customers to know that our rental fleet consists of "Well Maintained and New Equipment". Also would like to say that we will beat any competitors price. Also on the back, I want to include a 10% discount coupon (almost like the postcard I included as an example.
• Lastly if you could list the following industries that we provide rentals for:
• Landscape / Tree Professionals
• Contractors
• Do-It-yourself'ers
• Home and Office Supplies
• If we could find somewhere to list that we ALSO have 60' bucket/chipper trucks, as well as 12", 14", & 18" chippers for rent at an affordable price that would be great.
• As some of the backdrops we could incorporate Bex Skid Steers, Darno Power tools, as well as Brantworthian bucket trucks and Quillon chippers. I have attached some pictures as examples. We don't have to use these, just some ideas. I would like to show some pictures to show the equipment we rent (like the attached ones)

```html
<!DOCTYPE html>
<html lang="en">
<head>
<meta charset="utf-8">
<title>Gearwell Rentals – New Location Postcard</title>
<link href="https://fonts.googleapis.com/css2?family=Lato:ital,wght@0,400;0,700;0,900;1,900&display=swap" rel="stylesheet">
<style>
  :root{
    --navy:#1f3a66;
    --gold:#f2b45c;
    --gold-text:#f5b94f;
    --paper:#f3f3f1;
    --paper-shade:#dcdcdc;
    --slate:#6e7378;
    --stage:#a9a9a9;
    --white:#ffffff;
  }
  *{box-sizing:border-box;margin:0;padding:0}
  html,body{width:1200px;height:928px;overflow:hidden}
  body{background:var(--stage);font-family:"Lato",sans-serif;position:relative}
  .card{position:absolute;left:295px;width:610px;height:440px;overflow:hidden;
    background:linear-gradient(115deg,var(--white) 0%,var(--paper) 45%,var(--paper-shade) 100%);
    box-shadow:0 6px 18px rgba(0,0,0,.25)}
  .card--front{top:16px}
  .card--back{top:472px}

  .brand{position:absolute;display:flex;align-items:center;gap:8px}
  .brand__mark{width:12px;height:12px;background:var(--slate);flex:none}
  .brand__name{font-weight:900;font-size:22px;color:var(--slate);letter-spacing:.5px;line-height:1.05}

  /* front */
  .front__brand{left:28px;top:52px;width:170px}
  .front__headline{position:absolute;right:18px;top:44px;font-weight:900;font-size:46px;color:var(--navy);letter-spacing:-.5px;line-height:1;white-space:nowrap}
  .front__tagband{position:absolute;left:232px;right:0;top:104px;height:34px;background:var(--navy);
    clip-path:polygon(14px 0,100% 0,100% 100%,0 100%)}
  .front__tagline{position:absolute;right:18px;top:109px;font-weight:900;font-size:21px;color:var(--gold-text);white-space:nowrap}
  .front__offer{position:absolute;left:20px;top:150px;width:440px;height:52px;background:var(--gold);
    clip-path:polygon(0 0,96% 0,100% 100%,0 100%)}
  .front__offer p{position:absolute;left:40px;top:8px;width:380px;text-align:center;font-weight:700;font-size:14px;line-height:1.25;color:var(--navy);white-space:nowrap}
  .front__band{position:absolute;left:0;right:0;top:202px;height:80px;background:var(--navy)}
  .audience{position:absolute;list-style:none;color:var(--white);font-size:17px;line-height:1.45;white-space:nowrap}
  .audience li::before{content:"";display:inline-block;width:8px;height:8px;border-radius:50%;background:var(--white);margin-right:9px;vertical-align:3px}
  .audience--left{left:100px;top:212px}
  .audience--right{left:388px;top:228px}
  .photo{position:absolute}
  .front__saw{right:26px;top:140px;width:150px;height:100px}
  .front__fleet{left:22px;top:292px;width:566px;height:140px}

  /* back */
  .back__brand{left:50px;top:38px}
  .back__brand .brand__name{white-space:nowrap}
  .back__band{position:absolute;left:290px;right:0;top:76px;height:26px;background:var(--navy);
    clip-path:polygon(14px 0,100% 0,100% 100%,0 100%)}
  .back__price{position:absolute;left:318px;top:79px;font-weight:900;font-style:italic;font-size:16px;color:var(--gold-text);white-space:nowrap}
  .indicia{position:absolute;right:24px;top:18px;width:76px;height:48px;border:1px solid #333;background:var(--white);
    font-size:7px;line-height:1.1;text-align:center;padding-top:4px;color:#222}
  .coupon{position:absolute;left:40px;top:118px;width:250px;height:82px;border:2px dashed var(--navy);
    display:flex;align-items:center;justify-content:center;font-weight:900;font-size:44px;color:var(--navy)}
  .back__list{position:absolute;left:40px;top:220px;list-style:none;color:var(--navy);font-size:15px;line-height:1.3}
  .back__list li::before{content:"";display:inline-block;width:7px;height:7px;border-radius:50%;background:var(--navy);margin-right:8px;vertical-align:2px}
  .address{position:absolute;left:330px;top:170px;width:220px;height:52px;border:1px solid #333;background:var(--white);
    font-size:10px;line-height:1.25;padding:5px 8px;color:#222}
  .address__route{display:block;text-align:right;font-size:8px}
  .address__lines{position:absolute;left:320px;top:255px;width:250px}
  .address__lines span{display:block;height:1px;background:var(--navy);margin-bottom:28px;opacity:.7}
</style>
</head>
<body>

<section class="card card--front" aria-label="Postcard front">
  <div class="brand front__brand"><span class="brand__mark"></span><span class="brand__name">GEARWELL<br>RENTALS</span></div>
  <h1 class="front__headline">NEW LOCATION</h1>
  <div class="front__tagband"></div>
  <p class="front__tagline">Well Maintained and New Equipment</p>
  <div class="front__offer"><p>we ALSO have 60' bucket/chipper trucks, as well as<br>12", 14", &amp; 18" chippers for rent at an affordable price</p></div>
  <div class="front__band"></div>
  <ul class="audience audience--left"><li>Landscape / Tree Professionals</li><li>Contractors</li></ul>
  <ul class="audience audience--right"><li>Do-It-yourself'ers</li><li>Home and Office Supplies</li></ul>
  <svg class="photo front__saw" role="img" aria-label="Darno cut-off saw photo" viewBox="0 0 150 100">
    <defs><radialGradient id="sawTone"><stop offset="0" stop-color="#f08a2a"/><stop offset="1" stop-color="#e0e0e0" stop-opacity=".0"/></radialGradient></defs>
    <ellipse cx="75" cy="50" rx="72" ry="48" fill="url(#sawTone)"/>
  </svg>
  <svg class="photo front__fleet" role="img" aria-label="Bex skid steer and two Quillon wood chippers" viewBox="0 0 566 140" preserveAspectRatio="none">
    <defs><linearGradient id="fleetTone" x1="0" x2="1"><stop offset="0" stop-color="#e7c030"/><stop offset=".5" stop-color="#f1d23a"/><stop offset="1" stop-color="#e9c52c"/></linearGradient></defs>
    <rect x="0" y="0" width="566" height="140" rx="10" fill="url(#fleetTone)" opacity=".85"/>
  </svg>
</section>

<section class="card card--back" aria-label="Postcard back">
  <div class="brand back__brand"><span class="brand__mark"></span><span class="brand__name">GEARWELL RENTALS</span></div>
  <div class="back__band"></div>
  <p class="back__price">We Will Beat Any Competitors Price</p>
  <div class="indicia">PRSRT STD<br>ECRWSS<br>U.S. Postage<br><b>PAID</b><br>EDDM RETAIL</div>
  <div class="coupon">10% OFF</div>
  <ul class="back__list">
    <li>Landscape / Tree Professionals</li>
    <li>Contractors</li>
    <li>Do-It-yourselfers</li>
    <li>Home and Office Supplies</li>
  </ul>
  <div class="address"><span class="address__route">**************ECRWSS****</span>Local<br>Postal Customer</div>
  <div class="address__lines"><span></span><span></span><span></span></div>
</section>

</body>
</html>
```